Business Card Design for a Technology Development Company

******* PLEASE NOTE (ALL DESIGNERS): I am going to finish the competition on Monday the 9th July (NOT SATURDAY 15TH). I have some designs I like and need to get them printed next week. Please submit any designs today or tomorrow. *******

PLEASE READ ALL OF THE REQUIREMENTS!!! I've rejected lot's of designs in the past because they didn't read the basic requirements - thanks and good luck!

Quill Harbor is a UK technology / small holding company that invests in startups and develops new ideas. In addition it provides IT Professional Services.

Ideally the design will be simple, professional, smart, and sophisticated, and overall be nice to look at. You can be creative as you like with the design, equally as simple as you like - you guys are the professionals so I'll leave it to your inspiration (make sure you incorporate the logo)!
Updates

PLEASE NOTE (ALL DESIGNERS): I am going to finish the competition on Monday the 9th July (NOT SATURDAY 15TH).  I have some designs I like and need to get them printed next week.  Please submit any designs today or tomorrow.

Target Market(s)

Enterprises / corporations / public sector / technical engineers / investors. More www.brantelix.com / www.vornel.com than www.pibbleroo.com!

Industry/Entity Type

Business

Requirements
Must have
• It should be modern and any artwork (if used) should be simple
- Pastel colours, dark and light colours, and shades are preferred over bright colours
- The design should incorporate the attached Quill Harbor logo and the logo colour scheme
- The logo should be on both sides. The back should just have the logo, maybe with some additional graphics
- It must have the following information on:

FirstName SecondName
Company Position
Email: name@quillharbor.co.uk
Mobile: +44 (0) 7700 984312

- The final design should be for a UK business card, dimensions: 85mm × 55mm
- The final design should have bleed marks to allow for printing and should be given in vector formats (EPS and AI)
Nice to have
• The Logo can be separated from the font in the logo on the front of the card. This isn't necessary or required, just to know it's not a limitation.
Should not have
• No bright colours (I prefer pastel colours, dark and light colours, and shades)
- Fonts that are to thin
- Effects or designs that make it difficult to print
- Italic or old fashioned looking fonts, i.e. anything like Times New Roman is a NO!

```html
<!DOCTYPE html>
<html lang="en">
<head>
<meta charset="utf-8">
<title>Quill Harbor – Business Cards</title>
<link rel="stylesheet" href="https://fonts.googleapis.com/css2?family=Open+Sans:wght@600;700;800&display=swap">
<style>
  :root {
    --page-bg: #e9eceb;
    --card-white: #ffffff;
    --teal: #1f8d96;
    --teal-dark: #0d6570;
    --teal-deep: #0a5660;
    --teal-light: #d6ecee;
    --teal-pale: #eef7f8;
    --silver-light: #e3e7e8;
    --silver-dark: #8f9a9c;
    --text-white: #ffffff;
  }
  * { box-sizing: border-box; margin: 0; padding: 0; }
  html, body {
    width: 1200px; height: 900px; overflow: hidden;
    background: var(--page-bg);
    font-family: "Open Sans", Arial, sans-serif;
  }
  .card {
    position: absolute;
    top: 269px;
    width: 560px; height: 362px;
    background: var(--card-white);
    overflow: hidden;
    box-shadow: 0 6px 18px rgba(0,0,0,0.18);
  }
  .card--back { left: 20px; }
  .card--front { left: 620px; }
  .card__shapes, .card__grid {
    position: absolute; inset: 0; width: 100%; height: 100%;
  }
  .logo {
    position: absolute;
    display: flex; align-items: center; gap: 10px;
    color: var(--teal-dark);
    font-weight: 800;
    font-size: 31px;
    letter-spacing: -0.5px;
    white-space: nowrap;
  }
  .logo__dot {
    width: 36px; height: 36px; border-radius: 50%;
    background: var(--teal);
    flex: none;
  }
  .card--back .logo { left: 30px; top: 72px; }
  .card--front .logo { left: 26px; top: 150px; font-size: 27px; }
  .card--front .logo__dot { width: 30px; height: 30px; }

  .product-photo {
    position: absolute;
    left: 190px; top: 130px;
    width: 170px; height: 175px;
    border-radius: 10px;
    background: radial-gradient(ellipse at 40% 35%, var(--silver-light), var(--silver-dark) 80%, rgba(143,154,156,0) 100%);
    opacity: 0.9;
  }

  .person {
    position: absolute; right: 28px; top: 72px;
    text-align: right;
  }
  .person__name {
    color: var(--teal);
    font-weight: 700; font-size: 27px; line-height: 1.15;
  }
  .person__role {
    color: var(--teal-dark);
    font-weight: 700; font-size: 16px; line-height: 1.3;
  }
  .contact {
    position: absolute; right: 28px; top: 270px;
    text-align: right;
    color: var(--text-white);
    font-weight: 700; font-size: 15px; line-height: 1.7;
    list-style: none;
  }
</style>
</head>
<body>

<section class="card card--back" aria-label="Card back">
  <svg class="card__shapes" viewBox="0 0 560 362" preserveAspectRatio="none" aria-hidden="true">
    <defs>
      <linearGradient id="backTeal" x1="0" y1="0" x2="0" y2="1">
        <stop offset="0" stop-color="var(--teal)"/>
        <stop offset="1" stop-color="var(--teal-dark)"/>
      </linearGradient>
    </defs>
    <path d="M0 238 C 180 150, 360 78, 560 22 L560 362 L0 362 Z" fill="var(--teal-deep)"/>
    <path d="M0 262 C 180 176, 360 104, 560 50 L560 362 L0 362 Z" fill="url(#backTeal)"/>
  </svg>
  <svg class="card__grid" viewBox="0 0 560 362" preserveAspectRatio="none" role="img" aria-label="Perspective grid pattern across the teal area">
    <defs>
      <linearGradient id="backGrid" x1="0" y1="0" x2="1" y2="1">
        <stop offset="0" stop-color="#ffffff" stop-opacity="0.05"/>
        <stop offset="1" stop-color="#ffffff" stop-opacity="0.16"/>
      </linearGradient>
    </defs>
    <path d="M0 262 C 180 176, 360 104, 560 50 L560 362 L0 362 Z" fill="url(#backGrid)"/>
  </svg>
  <div class="logo"><span class="logo__dot"></span><span class="logo__name">Quill Harbor</span></div>
  <div class="product-photo" role="img" aria-label="Photo of two silver USB cable connectors"></div>
</section>

<section class="card card--front" aria-label="Card front">
  <svg class="card__shapes" viewBox="0 0 560 362" preserveAspectRatio="none" aria-hidden="true">
    <defs>
      <linearGradient id="frontLight" x1="0" y1="0" x2="1" y2="0">
        <stop offset="0" stop-color="var(--card-white)"/>
        <stop offset="0.55" stop-color="var(--teal-pale)"/>
        <stop offset="1" stop-color="var(--teal-light)"/>
      </linearGradient>
      <linearGradient id="frontTeal" x1="0" y1="0" x2="0" y2="1">
        <stop offset="0" stop-color="var(--teal)"/>
        <stop offset="1" stop-color="var(--teal-dark)"/>
      </linearGradient>
    </defs>
    <path d="M0 230 C 200 140, 380 50, 560 0 L560 362 L0 362 Z" fill="url(#frontLight)"/>
    <path d="M0 290 C 200 232, 380 180, 560 150 L560 362 L0 362 Z" fill="var(--teal-deep)"/>
    <path d="M0 312 C 200 252, 380 200, 560 172 L560 362 L0 362 Z" fill="url(#frontTeal)"/>
  </svg>
  <svg class="card__grid" viewBox="0 0 560 362" preserveAspectRatio="none" role="img" aria-label="Perspective grid pattern across the teal area">
    <defs>
      <linearGradient id="frontGrid" x1="0" y1="0" x2="1" y2="1">
        <stop offset="0" stop-color="#ffffff" stop-opacity="0.04"/>
        <stop offset="1" stop-color="#ffffff" stop-opacity="0.14"/>
      </linearGradient>
    </defs>
    <path d="M0 312 C 200 252, 380 200, 560 172 L560 362 L0 362 Z" fill="url(#frontGrid)"/>
  </svg>
  <div class="logo"><span class="logo__dot"></span><span class="logo__name">Quill Harbor</span></div>
  <div class="person">
    <p class="person__name">First and Last Name</p>
    <p class="person__role">Company Position</p>
  </div>
  <ul class="contact">
    <li>Mobile: +44 (0) 7700 984312</li>
    <li>Email: name@quillharbor.co.uk</li>
  </ul>
</section>

</body>
</html>
```